Tirovel

We need a business card for our company is a holding for different business all are different we try to have some air of relax and fun in our projects we add pictures of the office to give you an idea od the mood of the business

Business

```html
<!DOCTYPE html>
<html lang="en">
<head>
<meta charset="utf-8">
<title>Tirovel business card</title>
<link rel="stylesheet" href="https://fonts.googleapis.com/css2?family=Archivo+Black&family=Archivo:wght@600&display=swap">
<style>
  :root {
    --page: #ecebe7;
    --card-yellow: #f3c800;
    --glow-light: #f7dc1e;
    --glow-deep: #f0bf00;
    --strip-yellow: #f7df3c;
    --ink-brown: #7b4e1f;
  }
  html, body {
    margin: 0;
    width: 1200px;
    height: 900px;
    overflow: hidden;
    background: var(--page);
  }
  .card {
    position: absolute;
    left: 180px;
    top: 190px;
    width: 840px;
    height: 520px;
    overflow: hidden;
    background: var(--card-yellow);
    box-shadow: 0 18px 40px rgba(0,0,0,0.18);
    font-family: "Archivo", Arial, sans-serif;
  }
  .card-artwork {
    position: absolute;
    inset: 0;
    background: radial-gradient(ellipse 60% 75% at 45% 50%, var(--glow-light) 0%, var(--card-yellow) 70%, var(--glow-deep) 100%);
  }
  .contact-strip {
    position: absolute;
    top: 0;
    left: 0;
    right: 0;
    height: 52px;
    padding-right: 28px;
    box-sizing: border-box;
    background: var(--strip-yellow);
    display: flex;
    justify-content: flex-end;
    align-items: center;
    gap: 34px;
    font-size: 15px;
    font-weight: 600;
    color: var(--ink-brown);
  }
  .contact-item {
    display: flex;
    align-items: center;
    gap: 8px;
  }
  .contact-dot {
    width: 12px;
    height: 12px;
    background: var(--ink-brown);
    border-radius: 2px;
  }
  .brand-name {
    position: absolute;
    left: 96px;
    top: 150px;
    margin: 0;
    font-family: "Archivo Black", "Arial Black", sans-serif;
    font-weight: 400;
    font-size: 150px;
    line-height: 0.8;
    letter-spacing: -6px;
    color: var(--ink-brown);
  }
  .brand-name span { display: block; }
  .brand-name .brand-second { padding-left: 40px; }
  .address {
    position: absolute;
    left: 470px;
    top: 162px;
    margin: 0;
    font-style: normal;
    font-size: 22px;
    font-weight: 600;
    line-height: 1.2;
    color: var(--ink-brown);
  }
</style>
</head>
<body>
  <section class="card" aria-label="Tirovel business card">
    <div class="card-artwork" role="img" aria-label="Decorative background artwork: a large warm yellow sun shape framed by a white curved band"></div>

    <div class="contact-strip">
      <span class="contact-item">dana@tirovel.com</span>
      <span class="contact-item"><span class="contact-dot"></span>Tirovel</span>
      <span class="contact-item"><span class="contact-dot"></span>Tirovel</span>
    </div>

    <h1 class="brand-name"><span>Tiro</span><span class="brand-second">vel</span></h1>

    <address class="address">14 Harrowgate Row Ashfield<br>Northbury nb4 2kd</address>
  </section>
</body>
</html>
```